Artwork flyer ( named LU MO RAY ) for my music festival

I need a flyer artwork created for my indie pop, rock, hip-hop and dance music festival as soon as possible. The festival is for ages 18 to 30. Need flyer to be able to be abstracted so i can export into different social media
sizes etc

Here is some information around the music festival details.

Title: LU MO RAY ( music festival)

Artists :
KIRO Fen
Mirela Post
TRGs
The Brindles
Zank Pods
Velvet Otter
Copper ah
Quiet Tundra

Venue: Harrowmere Paddock Club
Date: Saturday 25th March
Tickets: www.tikvarro.com.au

Logo Text

LUMO RAY ( or LU MO RAY)

```html
<!DOCTYPE html>
<html lang="en">
<head>
<meta charset="utf-8">
<title>LU MO RAY Music Festival – Flyer Variants</title>
<link rel="stylesheet" href="https://fonts.googleapis.com/css2?family=Archivo+Black&family=Roboto+Condensed:wght@700&display=swap">
<style>
  :root {
    --page: #ffffff;
    --ink: #111111;
    --title-pink: #e5008a;
    --title-teal: #12a59a;
    --title-white: #ffffff;
    --lineup-bg: #f2ee6e;
    --lineup-ink: #333333;
    --date-purple: #7b3f98;
    --frame-lavender: #9a97c9;
    --panel-tan: #d4b679;
    --frame-orange: #f39321;
    --panel-grey: #bebfc1;
  }
  html, body {
    margin: 0;
    padding: 0;
    width: 1200px;
    height: 1000px;
    overflow: hidden;
    background: var(--page);
  }
  .canvas { display: block; width: 1200px; height: 1000px; }

  .flyer--tan  { --frame: var(--frame-lavender); --panel: var(--panel-tan);  --info-ink: var(--ink); }
  .flyer--grey { --frame: var(--frame-orange);   --panel: var(--panel-grey); --info-ink: #ffffff; }

  .flyer__frame { fill: var(--frame); }
  .flyer__panel { fill: var(--panel); }

  .title {
    font-family: "Archivo Black", "Arial Black", sans-serif;
    stroke: var(--ink);
    stroke-width: 5px;
    paint-order: stroke;
    stroke-linejoin: round;
  }
  .title--name { fill: var(--title-pink); font-size: 100px; }
  .title--music { fill: var(--title-teal); font-size: 88px; }
  .title--festival { fill: var(--title-white); font-size: 88px; }

  .band-stop--dark { stop-color: var(--ink); }
  .band-stop--light { stop-color: var(--panel); }

  .lineup__bg { fill: var(--lineup-bg); }
  .lineup__divider { stroke: var(--ink); stroke-width: 3px; }
  .lineup__act {
    font-family: "Archivo Black", "Arial Black", sans-serif;
    font-size: 24px;
    letter-spacing: 0.6px;
    fill: var(--lineup-ink);
  }

  .rule { stroke: var(--ink); stroke-width: 4px; }

  .date {
    font-family: "Roboto Condensed", "Arial Narrow", sans-serif;
    font-weight: 700;
    fill: var(--date-purple);
  }
  .date__year { font-size: 84px; }
  .date__day  { font-size: 40px; }
  .date__sup  { font-size: 20px; }

  .info {
    font-family: "Roboto Condensed", "Arial Narrow", sans-serif;
    font-weight: 700;
    font-size: 29px;
    fill: var(--info-ink);
  }
</style>
</head>
<body>
<svg class="canvas" viewBox="0 0 1200 1000" xmlns="http://www.w3.org/2000/svg">

  <!-- Tan edition -->
  <g class="flyer flyer--tan">
    <defs>
      <linearGradient id="band-tan" x1="0" y1="0" x2="0" y2="1">
        <stop offset="0" class="band-stop--dark"/>
        <stop offset="1" class="band-stop--light"/>
      </linearGradient>
    </defs>
    <rect class="flyer__frame" x="30" y="107" width="556" height="788"/>
    <rect class="flyer__panel" x="42" y="121" width="532" height="760"/>

    <text class="title title--name" x="70" y="210" textLength="478" lengthAdjust="spacingAndGlyphs">LU MO RAY</text>
    <g class="title title--music">
      <text x="70" y="287">M</text>
      <text x="178" y="287">U</text>
      <text x="300" y="287">S</text>
      <text x="413" y="287">I</text>
      <text x="486" y="287">C</text>
    </g>
    <text class="title title--festival" x="70" y="362" textLength="478" lengthAdjust="spacingAndGlyphs">FESTIVAL</text>

    <rect class="pattern-band" x="70" y="372" width="478" height="76" fill="url(#band-tan)" role="img" aria-label="Decorative black and panel-coloured check pattern band"/>

    <g class="lineup">
      <rect class="lineup__bg" x="70" y="448" width="478" height="219"/>
      <line class="lineup__divider" x1="299" y1="456" x2="299" y2="656"/>
      <text class="lineup__act" x="92" y="488">KIRO Fen</text>
      <text class="lineup__act" x="92" y="541">Mirela Post</text>
      <text class="lineup__act" x="92" y="594">TRGs</text>
      <text class="lineup__act" x="92" y="646">The Brindles</text>
      <text class="lineup__act" x="310" y="488">Zank Pods</text>
      <text class="lineup__act" x="310" y="541">Velvet Otter</text>
      <text class="lineup__act" x="310" y="594">Copper ah</text>
      <text class="lineup__act" x="310" y="646">Quiet Tundra</text>
    </g>

    <line class="rule" x1="70" y1="679" x2="548" y2="679"/>
    <g class="date">
      <text class="date__year" x="126" y="765">2023</text>
      <text class="date__day" x="300" y="722">SATURDAY</text>
      <text class="date__day" x="300" y="770">25<tspan class="date__sup" dy="-18">TH</tspan><tspan dy="18">MARCH</tspan></text>
    </g>
    <line class="rule" x1="70" y1="780" x2="548" y2="780"/>
    <text class="info" x="309" y="812" text-anchor="middle">Tickets - www.tikvarro.com.au</text>
    <line class="rule" x1="70" y1="822" x2="548" y2="822"/>
    <text class="info" x="309" y="853" text-anchor="middle">Harrowmere Paddock Club</text>
    <line class="rule" x1="70" y1="864" x2="548" y2="864"/>
  </g>

  <!-- Grey edition -->
  <g class="flyer flyer--grey" transform="translate(589 0)">
    <defs>
      <linearGradient id="band-grey" x1="0" y1="0" x2="0" y2="1">
        <stop offset="0" class="band-stop--dark"/>
        <stop offset="1" class="band-stop--light"/>
      </linearGradient>
    </defs>
    <rect class="flyer__frame" x="29" y="107" width="556" height="790"/>
    <rect class="flyer__panel" x="43" y="121" width="528" height="762"/>

    <text class="title title--name" x="70" y="210" textLength="478" lengthAdjust="spacingAndGlyphs">LU MO RAY</text>
    <g class="title title--music">
      <text x="70" y="287">M</text>
      <text x="178" y="287">U</text>
      <text x="300" y="287">S</text>
      <text x="413" y="287">I</text>
      <text x="486" y="287">C</text>
    </g>
    <text class="title title--festival" x="70" y="362" textLength="478" lengthAdjust="spacingAndGlyphs">FESTIVAL</text>

    <rect class="pattern-band" x="70" y="374" width="478" height="76" fill="url(#band-grey)" role="img" aria-label="Decorative black and panel-coloured check pattern band"/>

    <g class="lineup">
      <rect class="lineup__bg" x="70" y="450" width="478" height="218"/>
      <line class="lineup__divider" x1="299" y1="458" x2="299" y2="657"/>
      <text class="lineup__act" x="92" y="490">KIRO Fen</text>
      <text class="lineup__act" x="92" y="543">Mirela Post</text>
      <text class="lineup__act" x="92" y="596">TRGs</text>
      <text class="lineup__act" x="92" y="648">The Brindles</text>
      <text class="lineup__act" x="310" y="490">Zank Pods</text>
      <text class="lineup__act" x="310" y="543">Velvet Otter</text>
      <text class="lineup__act" x="310" y="596">Copper ah</text>
      <text class="lineup__act" x="310" y="648">Quiet Tundra</text>
    </g>

    <line class="rule" x1="70" y1="680" x2="548" y2="680"/>
    <g class="date">
      <text class="date__year" x="126" y="766">2023</text>
      <text class="date__day" x="300" y="723">SATURDAY</text>
      <text class="date__day" x="300" y="771">25<tspan class="date__sup" dy="-18">TH</tspan><tspan dy="18">MARCH</tspan></text>
    </g>
    <line class="rule" x1="70" y1="782" x2="548" y2="782"/>
    <text class="info" x="309" y="813" text-anchor="middle">Tickets - www.tikvarro.com.au</text>
    <line class="rule" x1="70" y1="824" x2="548" y2="824"/>
    <text class="info" x="309" y="855" text-anchor="middle">Harrowmere Paddock Club</text>
    <line class="rule" x1="70" y1="866" x2="548" y2="866"/>
  </g>

</svg>
</body>
</html>
```